Business Card Design Project

Cyber Security. Company name is brightHarbor.

Industry/Entity Type

Computer Security

Contact Information for Business Card

Gregory Lindqvist
Founder and Chief Hacker

2370 W. Alder Rd.
Suite 514
Chicago, IL 60482
773.555.0196
gregory.lindqvist@brightharbor.example
www.brightharbor.example

```html
<!DOCTYPE html>
<html lang="en">
<head>
<meta charset="utf-8">
<title>brightHarbor Business Card</title>
<link rel="stylesheet" href="https://fonts.googleapis.com/css2?family=Montserrat:ital,wght@0,400;0,500;0,700;1,400;1,500;1,700&display=swap">
<style>
  :root {
    --page-bg: #2a2a2a;
    --card-bg: #151515;
    --accent: #e3df57;
    --accent-soft: rgba(227, 223, 87, 0.35);
  }
  * { box-sizing: border-box; margin: 0; padding: 0; }
  html, body {
    width: 1200px; height: 900px; overflow: hidden;
    background: var(--page-bg);
    font-family: "Montserrat", Arial, sans-serif;
    color: var(--accent);
  }
  .canvas { position: relative; width: 1200px; height: 900px; }
  .card {
    position: absolute; left: 270px;
    width: 660px; height: 377px;
    background: var(--card-bg);
    box-shadow: 0 10px 30px rgba(0,0,0,0.5);
  }
  .card--front { top: 40px; }
  .card--back { top: 463px; }

  /* Front */
  .brand {
    position: absolute; top: 112px; left: 0; width: 100%;
    display: flex; justify-content: center; align-items: center; gap: 18px;
  }
  .brand__dot { width: 58px; height: 58px; border-radius: 50%; background: var(--accent); }
  .brand__name { font-size: 56px; font-weight: 500; letter-spacing: 1px; }
  .website {
    position: absolute; top: 254px; left: 0; width: 100%;
    display: flex; justify-content: center; align-items: center; gap: 12px;
    font-size: 17px; font-weight: 700; letter-spacing: 0.5px;
  }
  .website__dot { width: 22px; height: 22px; border-radius: 50%; background: var(--accent); }

  /* Back */
  .holder { position: absolute; top: 30px; left: 38px; }
  .holder__name { font-size: 31px; font-weight: 700; font-style: italic; line-height: 1.1; }
  .holder__title { font-size: 13px; font-style: italic; font-weight: 500; margin-top: 2px; }
  .holder__rule { position: absolute; top: 97px; left: 30px; width: 225px; height: 5px; background: var(--accent); }

  .service-icons { position: absolute; top: 205px; left: 40px; display: flex; gap: 24px; align-items: center; }
  .service-icons svg { width: 40px; height: 40px; display: block; }
  .service-icons__dot { width: 36px; height: 36px; border-radius: 50%; background: var(--accent); }

  .protection-art {
    position: absolute; top: 92px; left: 470px; width: 170px; height: 158px;
    background: radial-gradient(ellipse at 50% 45%, var(--accent) 0%, var(--accent-soft) 55%, transparent 80%);
  }
  .divider { position: absolute; top: 252px; left: 30px; width: 615px; height: 2px; background: var(--accent); }

  .contacts { position: absolute; top: 266px; left: 30px; list-style: none; }
  .contacts li { display: flex; align-items: center; gap: 12px; font-style: italic; font-weight: 500; }
  .contacts svg { width: 18px; height: 18px; flex: none; fill: var(--accent); }
  .contacts__phone { font-size: 17px; height: 28px; }
  .contacts__email { font-size: 20px; height: 36px; }
  .contacts__address { font-size: 19px; height: 44px; }
</style>
</head>
<body>
<main class="canvas">
  <section class="card card--front">
    <div class="brand">
      <span class="brand__dot"></span>
      <span class="brand__name">brightHarbor</span>
    </div>
    <div class="website">
      <span class="website__dot"></span>
      <span>www.brightharbor.example</span>
    </div>
  </section>

  <section class="card card--back">
    <div class="holder">
      <h1 class="holder__name">Gregory Lindqvist</h1>
      <p class="holder__title">Founder and Chief Hacker</p>
    </div>
    <div class="holder__rule"></div>

    <div class="service-icons">
      <svg viewBox="0 0 40 40" aria-label="Globe">
        <circle cx="20" cy="20" r="17" fill="none" stroke="var(--accent)" stroke-width="3"/>
        <path d="M9 13 q6 -3 10 2 q-2 5 2 8 q-1 6 -5 9 q-4 -6 -7 -10 z M24 8 q6 2 9 9 q-5 1 -6 -3 q-3 -1 -3 -6 z M26 24 q5 0 6 2 q-2 5 -7 7 q-1 -5 1 -9 z" fill="var(--accent)"/>
      </svg>
      <svg viewBox="0 0 40 40" aria-label="Tick">
        <path d="M4 21 l10 10 l22 -20" fill="none" stroke="var(--accent)" stroke-width="7" stroke-linejoin="round"/>
      </svg>
      <span class="service-icons__dot"></span>
    </div>

    <div class="protection-art" role="img" aria-label="Illustration of two hands holding a security shield"></div>
    <div class="divider"></div>

    <ul class="contacts">
      <li class="contacts__phone">
        <svg viewBox="0 0 24 24"><path d="M6.6 10.8a15 15 0 0 0 6.6 6.6l2.2-2.2c.3-.3.7-.4 1-.2 1.1.4 2.3.6 3.6.6.6 0 1 .4 1 1V20c0 .6-.4 1-1 1A17 17 0 0 1 3 4c0-.6.4-1 1-1h3.5c.6 0 1 .4 1 1 0 1.3.2 2.5.6 3.6.1.3 0 .7-.2 1z"/></svg>
        <span>773.555.0196</span>
      </li>
      <li class="contacts__email">
        <svg viewBox="0 0 24 24"><path d="M3 5h18v14H3z M5 7v.3l7 5 7-5V7z M19 9.7l-7 5-7-5V17h14z" fill-rule="evenodd"/></svg>
        <span>gregory.lindqvist@brightharbor.example</span>
      </li>
      <li class="contacts__address">
        <svg viewBox="0 0 24 24"><path d="M12 2a7 7 0 0 0-7 7c0 5 7 13 7 13s7-8 7-13a7 7 0 0 0-7-7zm0 9.5a2.5 2.5 0 1 1 0-5 2.5 2.5 0 0 1 0 5z"/></svg>
        <span>2370 W. Alder Rd. Suite 514 Chicago, IL 60482</span>
      </li>
    </ul>
  </section>
</main>
</body>
</html>
```